Stonebrook Glazeworks Inc. Business Card

Looking for business card with embossed raised logo print. Logo provided and want it to be most prominent image on card. Color pallet of black, red, white or charcoal gray preferred for brand recognition. Simple contact information on front and list description of services provided on back. Services included....Custom Showers, Tub Surrounds, Backsplashes, Fireplaces, Floors and more. Dustless Demolition, Lifetime Warranty, Proud member of the Federated Surface Installers Guild

Target Market(s)

High end residential remodel work and new home builders

Contact Information for Business Card

Phone # (402) 555-0193 email address, Stonebrookgw@mailvane.net Dorian Kovalski Owner

Requirements
Must have
• Business logo as most prominent image on the front of business card. Along with contact information and name Dorian Kovalski. Would like to see services provided on the back of the card.

```html
<!DOCTYPE html>
<html lang="en">
<head>
<meta charset="utf-8">
<title>Stonebrook Glazeworks Inc. Business Card</title>
<link rel="stylesheet" href="https://fonts.googleapis.com/css2?family=Montserrat:wght@400;500;600;700&display=swap">
<style>
  :root {
    --stage: #3a3b40;
    --black: #1c1c1e;
    --red: #dc2027;
    --red-light: #ee5a4f;
    --red-dark: #b5141b;
    --white: #ffffff;
    --charcoal: #3b3b3d;
  }
  * { margin: 0; padding: 0; box-sizing: border-box; }
  html, body { width: 1200px; height: 913px; overflow: hidden; }
  body {
    background: var(--stage);
    font-family: "Montserrat", sans-serif;
    position: relative;
  }
  .card {
    position: absolute;
    width: 620px;
    height: 354px;
    border-radius: 14px;
    overflow: hidden;
    box-shadow: 0 10px 28px rgba(0,0,0,.45);
  }
  .card-back { left: 60px; top: 70px; background: var(--black); }
  .card-front { left: 520px; top: 500px; background: var(--white); }
  .band { position: absolute; inset: 0; width: 100%; height: 100%; }
  .tile-artwork {
    position: absolute;
    left: 18px; top: 18px;
    width: 250px; height: 318px;
    border-radius: 10px;
    background: linear-gradient(120deg, var(--red-dark) 0%, var(--red) 40%, var(--red-light) 55%, var(--red) 70%);
  }
  .brand {
    position: absolute;
    display: flex;
    align-items: center;
    gap: 10px;
    color: var(--red);
    font-weight: 600;
    text-transform: uppercase;
    line-height: 1.05;
  }
  .brand-mark { width: 30px; height: 30px; background: var(--red); flex: none; }
  .brand-name { letter-spacing: 1px; }
  .card-back .brand { right: 36px; top: 48px; font-size: 30px; }
  .card-back .brand-name small { display: block; font-size: 15px; letter-spacing: 4px; }
  .card-front .brand { right: 36px; top: 30px; font-size: 24px; }
  .card-front .brand-name small { display: block; font-size: 12px; letter-spacing: 3px; }
  .services {
    position: absolute;
    right: 30px; top: 196px;
    width: 320px;
    text-align: right;
    color: var(--white);
    font-size: 13px;
    line-height: 1.55;
  }
  .services-title { font-weight: 700; font-size: 15px; letter-spacing: 1px; margin-bottom: 4px; }
  .person {
    position: absolute;
    right: 36px; top: 102px;
    text-align: right;
  }
  .person-name { color: var(--red); font-weight: 700; font-size: 20px; letter-spacing: 1px; }
  .person-title { color: var(--charcoal); font-size: 13px; margin-top: 2px; }
  .address {
    position: absolute;
    right: 36px; top: 166px;
    text-align: right;
    color: var(--charcoal);
    font-size: 13px;
    line-height: 1.5;
  }
  .contact-list {
    position: absolute;
    right: 30px; top: 250px;
    list-style: none;
    text-align: right;
    color: var(--white);
    font-size: 13px;
    line-height: 1.7;
  }
  .contact-list li { display: flex; justify-content: flex-end; align-items: center; gap: 8px; }
  .contact-icon { width: 12px; height: 12px; fill: none; stroke: var(--white); stroke-width: 1.6; }
</style>
</head>
<body>

  <section class="card card-back" aria-label="Business card back">
    <svg class="band" viewBox="0 0 620 354" preserveAspectRatio="none" aria-hidden="true">
      <polygon points="280,190 620,150 620,354 230,354" fill="var(--red)"/>
    </svg>
    <div class="tile-artwork" role="img" aria-label="Large decorative glossy red tile mosaic artwork"></div>
    <div class="brand">
      <span class="brand-mark"></span>
      <span class="brand-name">Stonebrook<small>Glazeworks Inc</small></span>
    </div>
    <div class="services">
      <p class="services-title">SERVICES</p>
      <p>Custom Showers | Tub Surrounds | Backsplashes | Fireplaces</p>
      <p>Floors and more. Dustless Demolition | Lifetime Warranty</p>
      <p>Proud member of the FSIG!!</p>
    </div>
  </section>

  <section class="card card-front" aria-label="Business card front">
    <svg class="band" viewBox="0 0 620 354" preserveAspectRatio="none" aria-hidden="true">
      <polygon points="280,270 620,200 620,354 240,354" fill="var(--red)"/>
      <rect x="596" y="20" width="24" height="26" fill="var(--red)"/>
    </svg>
    <div class="tile-artwork" role="img" aria-label="Large decorative glossy red tile mosaic artwork"></div>
    <div class="brand">
      <span class="brand-mark"></span>
      <span class="brand-name">Stonebrook<small>Glazeworks Inc</small></span>
    </div>
    <div class="person">
      <p class="person-name">DORIAN KOVALSKI</p>
      <p class="person-title">Director</p>
    </div>
    <address class="address" style="font-style:normal">
      418 Harlow Ridge Road<br>
      Millbrook, NE 68001
    </address>
    <ul class="contact-list">
      <li>+1 (402) 555-0193
        <svg class="contact-icon" viewBox="0 0 12 12" aria-hidden="true"><path d="M2 1 L4.5 1 L5.5 3.5 L4 4.5 Q5 7 7.5 8 L8.5 6.5 L11 7.5 L11 10 Q6 11 2 6 Q1 3 2 1 Z"/></svg>
      </li>
      <li>Stonebrookgw@mailvane.net
        <svg class="contact-icon" viewBox="0 0 12 12" aria-hidden="true"><rect x="1" y="2.5" width="10" height="7"/><path d="M1 2.5 L6 6.5 L11 2.5"/></svg>
      </li>
      <li>www.stonebrookglaze.net
        <svg class="contact-icon" viewBox="0 0 12 12" aria-hidden="true"><circle cx="6" cy="6" r="5"/><path d="M1 6 H11 M6 1 Q3 6 6 11 Q9 6 6 1"/></svg>
      </li>
    </ul>
  </section>

</body>
</html>
```